Professional, Attractive, Simple Website Needed!!

We completed the design for our logo.

We need a website built out around this.

Here are a couple samples of how we want ours formatted.

http://brvntapower.com

http://www.halvorbeam.com/lp/free-quote?LeadSource=Search%20Engine&ProgramName=webquery&experience=qual&language=en&type=brd&gclid=Xq7RTPwmEYKDLAvUHbsNQkfPZrTcGwnJuoVbXeLqHmRYdAsWtPkMcNfBYgzTrUoQJhEdWvKpYaLsZbCmNDgQwTxAoKpXbT_qkR

http://morvalo.co

Reason: Extending this deadline due to our delay in providing designers with content for each page. This is coming in next 24 hours.

Reason: Due to scheduling conflicts and extended travel delays related to Puerto Rico, the deadline has been extended. Your patience is greatly appreciated.

Reason: Travel and scheduling conflicts have made it impossible to give this project the thorough review it deserves, therefore I am extending the deadline. Thank you for your patience!

Target Market(s)

Home Owners who earn 60k + household annually

Industry/Entity Type

It Professional

Coding

Coded - Design and coding required

Number of Pages Required

5+ page

Font styles to use
Serif

Colors
34a7d8
9bcb3c

Requirements
Must have
• Simple
• Lead form Entry (Ability for visitor to enter Name, number and address for a quote)
• Sleek Design
• Professional
• Testimonials
• Use color Scheme of Design Logo Attached
Nice to have
• Video when site starts
• Like this
• https://www.vidmarrow.com/watch?v=qT8mRpXw2Ka&feature=vidm.ro
Should not have
• Should not include Commercial solar
• Should not include wind power

```html
<!DOCTYPE html>
<html lang="en">
<head>
<meta charset="utf-8">
<title>Sunward Energy – Renewable Energy</title>
<link href="https://fonts.googleapis.com/css2?family=Roboto:wght@300;400;500;700&family=Quicksand:wght@600;700&display=swap" rel="stylesheet">
<style>
:root{
  --blue:#0d8ed4;
  --blue-dark:#0a77b4;
  --green:#9bcb3c;
  --green-dark:#86b52c;
  --sky:#d4e7f7;
  --ink:#2b2b2b;
  --text:#555;
  --muted:#999;
  --line:#e6e6e6;
  --panel:#f3f3f3;
  --white:#fff;
}
*{box-sizing:border-box;margin:0;padding:0}
html,body{width:1200px;height:3226px;overflow:hidden}
body{position:relative;background:var(--white);font-family:"Roboto",Arial,sans-serif;color:var(--text)}
.abs{position:absolute}

/* top contact tab */
.contact-tab{left:731px;top:0;width:469px;height:30px;background:var(--blue);clip-path:polygon(28px 0,100% 0,100% 100%,0 100%);color:#fff;font-size:11px;display:flex;align-items:center;gap:40px;padding-left:70px}
.contact-tab span{display:flex;align-items:center;gap:8px}

/* header */
.logo{left:88px;top:34px;display:flex;align-items:center;gap:12px}
.logo-dot{width:54px;height:54px;border-radius:50%;background:var(--blue)}
.logo-name{font-family:"Roboto",sans-serif;font-weight:500;font-size:26px;color:var(--blue);letter-spacing:.5px}
.nav{right:88px;top:62px;display:flex;gap:34px;font-size:12px;font-weight:500;color:#333;text-transform:uppercase}
.nav .active{color:var(--green)}

/* hero */
.hero{left:0;top:112px;width:1200px;height:600px}
.hero-eyebrow{left:88px;top:275px;font-family:"Quicksand",sans-serif;font-style:italic;font-weight:700;font-size:21px;color:var(--ink)}
.hero-title{left:86px;top:300px;font-family:"Quicksand",sans-serif;font-weight:700;font-size:64px;color:var(--ink);letter-spacing:-.5px}
.hero-title em{font-style:normal;color:var(--green)}
.hero-text{left:88px;top:378px;width:460px;font-size:12.5px;line-height:20px;color:#444}
.btn-video{left:88px;top:443px;width:151px;height:42px;background:var(--blue);color:#fff;font-size:11px;font-weight:500;text-transform:uppercase;display:flex;align-items:center;justify-content:center;gap:10px}
.hero-art{left:752px;top:250px;width:366px;height:360px;background:linear-gradient(180deg,#c9dced 0%,#ee6c3e 55%,#5cb85c 100%);border-radius:6px 6px 0 0}
.mouse{left:589px;top:660px;width:22px;height:34px;border:2px solid #b8c8d6;border-radius:11px}

/* request form */
.quote-card{left:725px;top:613px;width:387px;height:350px;background:#fff;box-shadow:0 8px 30px rgba(0,0,0,.12);padding:26px 34px}
.quote-card h3{font-weight:400;font-size:26px;color:var(--ink);text-align:center;margin-bottom:26px}
.field{height:44px;background:#f4f4f4;border:1px solid #ececec;margin-bottom:9px;display:flex;align-items:center;gap:12px;padding-left:18px;font-size:11px;color:#777}
.btn-quote{margin:20px auto 0;width:124px;height:42px;background:var(--green);color:#fff;font-size:11px;font-weight:500;text-transform:uppercase;display:flex;align-items:center;justify-content:center}

/* how it works */
.how-title{left:88px;top:736px;font-size:26px;color:var(--ink);font-weight:400}
.how-rule{left:88px;top:786px;width:34px;height:2px;background:var(--line)}
.step{top:842px;width:150px;text-align:center;font-size:12px;line-height:17px;color:#444}
.step-icon{width:82px;height:82px;border-radius:50%;border:1px solid var(--line);margin:0 auto 16px;display:flex;align-items:center;justify-content:center}

/* news */
.news-band{left:0;top:1058px;width:1200px;height:640px;background:var(--panel)}
.section-title{width:1200px;left:0;text-align:center;font-size:27px;font-weight:400;color:var(--ink)}
.news-card{top:1219px;width:328px;height:381px;background:#fff;box-shadow:0 2px 10px rgba(0,0,0,.06)}
.news-card.raised{box-shadow:0 22px 30px -14px rgba(0,0,0,.25)}
.news-img{height:256px}
.news-date{position:absolute;left:12px;top:12px;background:#fff;font-size:10px;padding:5px 10px;color:#444}
.news-body{padding:22px 28px}
.news-body h4{font-size:13px;font-weight:500;color:#222;margin-bottom:8px}
.news-body p{font-size:12px;color:#555}
.news-more{position:absolute;right:26px;bottom:26px;font-size:11px;color:var(--muted);display:flex;align-items:center;gap:6px}
.news-more i{width:16px;height:16px;border-radius:50%;background:#bbb;display:inline-block}
.news-card.raised .news-more{color:var(--blue)}
.news-card.raised .news-more i{background:var(--blue)}
.next-arrow{left:1136px;top:1355px;width:42px;height:42px;border-radius:50%;background:#fff;box-shadow:0 2px 8px rgba(0,0,0,.12);display:flex;align-items:center;justify-content:center}

/* green band */
.save-band{left:0;top:1698px;width:1200px;height:398px;background:linear-gradient(180deg,#a6d04a 0%,#92c43a 60%,#8bbf34 100%)}
.save-title{top:1790px;left:0;width:1200px;text-align:center;color:#fff;font-size:27px;font-weight:400}
.save-text{top:1858px;left:220px;width:760px;text-align:center;color:#fff;font-size:12px;line-height:21px}
.btn-more{left:540px;top:1913px;width:120px;height:38px;background:var(--blue);color:#fff;font-size:11px;font-weight:500;text-transform:uppercase;display:flex;align-items:center;justify-content:center}
.bulb-art{left:430px;top:1978px;width:340px;height:245px;border-radius:50% 50% 40% 40%;background:radial-gradient(ellipse at 45% 45%,#eef4f8 0%,#b9cbd6 50%,#6a9a3a 85%,#dfe5e8 100%)}

/* testimonials */
.story{top:2365px;width:316px;height:215px;background:#fff;box-shadow:0 3px 14px rgba(0,0,0,.09);padding:30px 32px}
.story p{font-size:12px;line-height:20px;color:#444}
.story-person{display:flex;align-items:center;gap:14px;margin-top:24px}
.avatar{width:52px;height:52px;border-radius:50%;background:#cfd5da}
.story-name{font-size:13px;color:var(--green)}
.story-handle{font-size:11px;color:#777}
.quote-mark{position:absolute;right:36px;bottom:36px;font-family:Georgia,serif;font-size:70px;line-height:1;color:#e4e4e4}
.pager{left:1135px;top:2440px;font-size:11px;color:#333}
.pager div{display:flex;align-items:center;gap:8px;height:22px}
.pager b{font-weight:400;width:10px}
.pager i{width:30px;height:1px;background:#999;display:inline-block}
.pager .on{color:var(--green)}
.pager .on i{background:var(--green)}

/* zip band */
.zip-band{left:0;top:2683px;width:1200px;height:151px;background:#f5f5f5}
.zip-text{left:88px;top:2727px;font-size:26px;line-height:31px;color:#222;font-weight:400}
.zip-input{left:656px;top:2735px;width:344px;height:49px;background:#fff;font-size:11px;color:#666;display:flex;align-items:center;padding-left:24px}
.btn-start{left:1000px;top:2735px;width:111px;height:49px;background:var(--green);color:#fff;font-size:11px;font-weight:500;text-transform:uppercase;display:flex;align-items:center;justify-content:center}

/* footer */
.footer{left:0;top:2834px;width:1200px;height:344px;background:var(--blue)}
.footer-logo{left:88px;top:2924px;display:flex;align-items:center;gap:14px}
.footer-logo .logo-dot{background:#fff;width:68px;height:68px}
.footer-logo .logo-name{color:#fff;font-size:28px}
.footer-about{left:88px;top:3008px;width:320px;color:#fff;font-size:12px;line-height:20px}
.footer-col{top:2920px;color:#fff}
.footer-col h5{font-size:16px;font-weight:400;margin-bottom:16px}
.footer-col li{list-style:none;font-size:12px;height:28.6px;display:flex;align-items:center;gap:10px}
.footer-col li i{width:10px;height:10px;border-radius:50%;background:#fff;display:inline-block}
.copyright{left:0;top:3178px;width:1200px;height:48px;background:var(--blue-dark);color:#fff;font-size:12px;display:flex;align-items:center;justify-content:center}
.to-top{left:1133px;top:3175px;width:44px;height:44px;border-radius:50%;background:#fff;box-shadow:0 2px 8px rgba(0,0,0,.2);display:flex;align-items:center;justify-content:center}
</style>
</head>
<body>

<!-- top contact tab -->
<div class="abs contact-tab">
  <span><svg width="11" height="11" viewBox="0 0 24 24" fill="#fff"><path d="M6.6 10.8a15 15 0 0 0 6.6 6.6l2.2-2.2c.3-.3.7-.4 1-.2 1.1.4 2.3.6 3.6.6.6 0 1 .4 1 1V20c0 .6-.4 1-1 1A17 17 0 0 1 3 4c0-.6.4-1 1-1h3.5c.6 0 1 .4 1 1 0 1.3.2 2.5.6 3.6.1.3 0 .7-.2 1z"/></svg>Call Us +08 555 010 2040</span>
  <span><svg width="12" height="10" viewBox="0 0 24 18" fill="#fff"><path d="M0 0h24v18H0z" opacity=".0"/><path d="M1 1h22v16H1z" fill="none" stroke="#fff" stroke-width="2"/><path d="M1 1l11 9 11-9" fill="none" stroke="#fff" stroke-width="2"/></svg>hello@sunwardhome.net</span>
</div>

<!-- header -->
<div class="abs logo"><span class="logo-dot"></span><span class="logo-name">SUNWARD ENERGY</span></div>
<nav class="abs nav">
  <span class="active">Home</span><span>About Us</span><span>Partnerships</span><span>Testimonials</span><span>Blog</span><span>FAQ</span><span>Contact Us</span>
</nav>

<!-- hero -->
<svg class="abs hero" width="1200" height="600" viewBox="0 0 1200 600">
  <polygon points="0,0 1200,0 1200,480 602,598 0,480" fill="#d4e7f7"/>
</svg>
<div class="abs hero-art" role="img" aria-label="Illustration of an orange house with a dark roof in front of pale city buildings, with green shrubs"></div>
<div class="abs hero-eyebrow">Sunward Energy Advantages</div>
<div class="abs hero-title">Renewable <em>Energy</em></div>
<p class="abs hero-text">Aenean sollicitudin, lorem quis bibendum auctor nisi elit consequat ipsum nec sagittis sem nibh id elit duis sed odio sit...</p>
<div class="abs btn-video"><svg width="10" height="11" viewBox="0 0 10 11"><path d="M0 0l10 5.5L0 11z" fill="#fff"/></svg>Watch a Video</div>
<div class="abs mouse"></div>

<!-- request form -->
<div class="abs quote-card">
  <h3>Request Information</h3>
  <div class="field"><svg width="10" height="11" viewBox="0 0 10 11" fill="#aaa"><circle cx="5" cy="3" r="2.6"/><path d="M0 11c0-3 2.2-4.6 5-4.6S10 8 10 11z"/></svg>Enter your name...</div>
  <div class="field"><svg width="10" height="10" viewBox="0 0 24 24" fill="#aaa"><path d="M6.6 10.8a15 15 0 0 0 6.6 6.6l2.2-2.2c.3-.3.7-.4 1-.2 1.1.4 2.3.6 3.6.6.6 0 1 .4 1 1V20c0 .6-.4 1-1 1A17 17 0 0 1 3 4c0-.6.4-1 1-1h3.5c.6 0 1 .4 1 1 0 1.3.2 2.5.6 3.6.1.3 0 .7-.2 1z"/></svg>Enter your number...</div>
  <div class="field"><svg width="9" height="12" viewBox="0 0 9 12" fill="#aaa"><path d="M4.5 0A4.5 4.5 0 0 0 0 4.5C0 8 4.5 12 4.5 12S9 8 9 4.5A4.5 4.5 0 0 0 4.5 0zm0 6.2a1.7 1.7 0 1 1 0-3.4 1.7 1.7 0 0 1 0 3.4z"/></svg>Enter your address</div>
  <div class="btn-quote">For a Quote</div>
</div>

<!-- how it works -->
<h2 class="abs how-title">How it Works...</h2>
<div class="abs how-rule"></div>
<div class="abs step" style="left:58px"><div class="step-icon"><svg width="34" height="34" viewBox="0 0 34 34" fill="none" stroke="#9bcb3c" stroke-width="2"><path d="M6 20v-3a11 11 0 0 1 22 0v3"/><rect x="4" y="19" width="6" height="10" rx="2"/><rect x="24" y="19" width="6" height="10" rx="2"/></svg></div>Speak to a solar<br>Consultant</div>
<div class="abs step" style="left:211px"><div class="step-icon"><svg width="34" height="34" viewBox="0 0 34 34" fill="none" stroke="#9bcb3c" stroke-width="2"><rect x="9" y="4" width="7" height="26" rx="1"/><path d="M20 6l5-2 2 24-5 2z"/><path d="M9 10h3M9 16h3M9 22h3"/></svg></div>We'll design your solar<br>panel system</div>
<div class="abs step" style="left:366px"><div class="step-icon"><svg width="34" height="34" viewBox="0 0 34 34" fill="none" stroke="#9bcb3c" stroke-width="2"><rect x="5" y="7" width="24" height="22" rx="2"/><path d="M5 13h24M11 4v6M23 4v6M10 18h3M16 18h3M22 18h3M10 23h3M16 23h3"/></svg></div>Schedule your 1 day<br>install</div>
<div class="abs step" style="left:518px"><div class="step-icon"><svg width="34" height="34" viewBox="0 0 34 34" fill="none" stroke="#9bcb3c" stroke-width="2"><circle cx="17" cy="17" r="12"/><path d="M21 12.5c-1-1.2-2.3-1.6-4-1.6-2 0-3.5 1-3.5 2.7 0 3.8 7.5 2 7.5 6 0 1.8-1.6 3-4 3-1.8 0-3.3-.6-4.2-1.8M17 8.5v2.4M17 23v2.4"/></svg></div>Start saving on your<br>electricity bill</div>

<!-- news -->
<div class="abs news-band"></div>
<h2 class="abs section-title" style="top:1138px">Stay Up To Date Recent News</h2>
<article class="abs news-card" style="left:88px">
  <div class="news-img" role="img" aria-label="Photo of two hanging light bulbs against a blue cloudy sky" style="background:linear-gradient(180deg,#3f78c2,#a9c6e4 70%,#e2ebf3)"></div>
  <span class="news-date">▦ 25/05/2017</span>
  <div class="news-body"><h4>Some Heading News Goes Here...</h4><p>Lorem ipsum is simpmy dummy text dummy...</p></div>
  <span class="news-more">View More <i></i></span>
</article>
<article class="abs news-card raised" style="left:436px">
  <div class="news-img" role="img" aria-label="Photo of green alpine meadows beneath mountains and a blue sky" style="background:linear-gradient(180deg,#5d95d4 0%,#b8cfe0 35%,#7a9a5a 55%,#6f9a38 100%)"></div>
  <span class="news-date">▦ 25/05/2017</span>
  <div class="news-body"><h4>Some Heading News Goes Here...</h4><p>Lorem ipsum is simpmy dummy text dummy...</p></div>
  <span class="news-more">View More <i></i></span>
</article>
<article class="abs news-card" style="left:783px">
  <div class="news-img" role="img" aria-label="Photo of a couple sitting on a lakeside jetty beside tall reeds" style="background:linear-gradient(180deg,#8fb7e0 0%,#5a8cbe 40%,#3f75a8 70%,#b79a6a 100%)"></div>
  <span class="news-date">▦ 25/05/2017</span>
  <div class="news-body"><h4>Some Heading News Goes Here...</h4><p>Lorem ipsum is simpmy dummy text dummy...</p></div>
  <span class="news-more">View More <i></i></span>
</article>
<div class="abs next-arrow"><svg width="14" height="12" viewBox="0 0 14 12" fill="none" stroke="#333" stroke-width="1.6"><path d="M0 6h12M7 1l5 5-5 5"/></svg></div>

<!-- green band -->
<div class="abs save-band" role="img" aria-label="Green-tinted photo of rolling fields with a lone figure walking"></div>
<h2 class="abs save-title">Save The Energy Planet!</h2>
<p class="abs save-text">Lorem Ipsum. Proin gravida nibh vel velit auctor aliquet aenean sollicitudin, orem quis bibendum auctor, nisi elit consequat ipsum nec sagittis sem nibh id elit duis sed odio sit amet nibh vulputate cursus a sit amet mauris.</p>
<div class="abs btn-more">View More</div>
<div class="abs bulb-art" role="img" aria-label="Photo of a glass light bulb lying on its side with green grass growing inside"></div>

<!-- testimonials -->
<h2 class="abs section-title" style="top:2280px">Success Stories</h2>
<div class="abs story" style="left:88px">
  <p>Aenean vulputate eleifend tellus aenean leo ligula porttitor eu, consequat vitae eleifend ac enim aliquam lorem ante .</p>
  <div class="story-person"><div class="avatar" role="img" aria-label="Customer portrait"></div><div><div class="story-name">Nila Varga</div><div class="story-handle">@nila</div></div></div>
  <span class="quote-mark">“</span>
</div>
<div class="abs story" style="left:439px">
  <p>Aenean vulputate eleifend tellus aenean leo ligula porttitor eu, consequat vitae eleifend ac enim aliquam lorem ante .</p>
  <div class="story-person"><div class="avatar" role="img" aria-label="Customer portrait"></div><div><div class="story-name">Omar Lenz</div><div class="story-handle">@omar</div></div></div>
  <span class="quote-mark">“</span>
</div>
<div class="abs story" style="left:789px">
  <p>Aenean vulputate eleifend tellus aenean leo ligula porttitor eu, consequat vitae eleifend ac enim aliquam lorem ante .</p>
  <div class="story-person"><div class="avatar" role="img" aria-label="Customer portrait"></div><div><div class="story-name">Rafe Collier</div><div class="story-handle">@rafe</div></div></div>
  <span class="quote-mark">“</span>
</div>
<div class="abs pager">
  <div><b>1</b><i></i></div>
  <div class="on"><b>2</b><i></i></div>
  <div><b>3</b><i></i></div>
</div>

<!-- zip band -->
<div class="abs zip-band"></div>
<div class="abs zip-text">Enter your zip code<br>to see if solar workers for you</div>
<div class="abs zip-input">Enter your zip code</div>
<div class="abs btn-start">Get Started</div>

<!-- footer -->
<footer class="abs footer"></footer>
<div class="abs footer-logo"><span class="logo-dot"></span><span class="logo-name">SUNWARD ENERGY</span></div>
<p class="abs footer-about">Aenean vulputate eleifend tellus aenean leo ligula porttitor eu, consequat vitae eleifend ac enim aliquam lorem ante ...</p>
<div class="abs footer-col" style="left:531px"><h5>Information</h5><ul><li>About us</li><li>Sitemap</li><li>Advanced Search</li><li>Bookings and Returns</li><li>Contact</li></ul></div>
<div class="abs footer-col" style="left:789px"><h5>My Account</h5><ul><li>Log In</li><li>History</li><li>Account</li><li>Track My Order</li><li>Help</li></ul></div>
<div class="abs footer-col" style="left:1034px"><h5>Follow us</h5><ul><li><i></i>Linkwall</li><li><i></i>Chirpline</li><li><i></i>Circleup</li><li><i></i>Snapframe</li></ul></div>
<div class="abs copyright">© 2017, All Rights Reserved.</div>
<div class="abs to-top"><svg width="12" height="14" viewBox="0 0 12 14" fill="none" stroke="#333" stroke-width="1.6"><path d="M6 14V2M1 7l5-5 5 5"/></svg></div>

</body>
</html>
```